A bar in Newtown, NSW needs a website

We need a website design for a small speakeasy-style bar in Newtown, NSW Australia. The website needs to be simple to navigate, minimalistic, and feature light colours.

The functionality has to be fairly simple:

Main page (navigates to things below)
Food menu
Beverage menu
Bookings

Social media links and misc info at the bottom of every page.

The menus pages need to have space for text inserted as a jpeg file.

Name and logo are attached.

Coded - Design and coding required

4 page

```html
<!DOCTYPE html>
<html lang="en">
<head>
<meta charset="utf-8">
<title>The Quiet Hound — Bar &amp; Kitchen</title>
<link href="https://fonts.googleapis.com/css2?family=Cinzel:wght@400;600&family=Open+Sans:wght@400;600;700&display=swap" rel="stylesheet">
<style>
:root{
  --black:#0c0c0c;
  --ink:#222222;
  --muted:#6f6f6f;
  --light:#f4f4f4;
  --line:#e2e2e2;
  --yellow:#f5b81c;
  --white:#ffffff;
  --field:#f3f3f3;
  --panel:rgba(8,8,8,.72);
}
*{box-sizing:border-box;margin:0;padding:0}
html,body{width:1200px;height:3147px;overflow:hidden}
body{font-family:"Open Sans",Arial,sans-serif;color:var(--ink);background:var(--white);position:relative}
section,header,footer{position:absolute;left:0;width:1200px}

/* header */
.site-header{top:0;height:84px;background:var(--black);z-index:5}
.brand-small{position:absolute;left:164px;top:18px;color:var(--white);font-family:"Cinzel",Georgia,serif;font-size:17px;line-height:19px;font-weight:600;letter-spacing:1px}
.nav{position:absolute;left:496px;top:0;height:84px;display:flex}
.nav a{color:var(--white);text-decoration:none;font-size:12.5px;font-weight:700;letter-spacing:.3px;line-height:84px;position:relative;margin-right:56px}
.nav a.active::after{content:"";position:absolute;left:50%;bottom:0;margin-left:-6px;border:6px solid transparent;border-bottom-color:var(--white)}
.search{position:absolute;left:998px;top:22px;width:40px;height:40px;border-radius:50%;background:var(--white)}

/* hero */
.hero{top:84px;height:598px;background:linear-gradient(160deg,#8a7a63 0%,#5e5546 35%,#3b352e 70%,#2a2622 100%)}
.hero-photo{position:absolute;inset:0;background:radial-gradient(ellipse at 30% 30%,rgba(230,200,150,.35),transparent 60%),radial-gradient(ellipse at 80% 40%,rgba(200,180,150,.25),transparent 55%)}
.hero-shade{position:absolute;inset:0;background:rgba(0,0,0,.35)}
.hero-logo{position:absolute;top:116px;width:100%;text-align:center;color:var(--white);font-family:"Cinzel",Georgia,serif;font-weight:600}
.hero-logo .the{font-size:34px;letter-spacing:2px;display:block;line-height:40px}
.hero-logo .name{font-size:56px;letter-spacing:2px;display:block;line-height:62px}
.hero-rule{position:absolute;top:264px;left:452px;width:296px;height:14px}
.hero-text{position:absolute;top:296px;width:100%;text-align:center;color:var(--white);font-size:17px;line-height:23px}
.btn-start{position:absolute;left:487px;top:373px;width:226px;height:51px;background:var(--yellow);color:var(--white);font-weight:700;font-size:16px;line-height:51px;text-align:center;border-right:5px solid var(--white)}
.dots{position:absolute;top:515px;left:580px;display:flex;gap:4px}
.dots i{width:12px;height:12px;border:2px solid var(--white);border-radius:50%;display:block}

/* shared section heading */
.sec-title{position:absolute;width:100%;text-align:center;font-family:"Cinzel",Georgia,serif;font-size:29px;letter-spacing:1px;color:var(--ink)}
.sec-intro{position:absolute;left:283px;width:634px;text-align:center;font-size:10.5px;line-height:23px;color:var(--muted)}
.dark .sec-title{color:var(--white)}
.dark .sec-intro{color:#bdbdbd}

/* food */
.food{top:682px;height:629px;background:var(--light)}
.deco-plate{position:absolute;border-radius:50%}
.tabs{position:absolute;top:164px;left:480px;display:flex;gap:4px}
.tabs span{height:25px;line-height:25px;padding:0 9px;font-size:10.5px;font-weight:700;background:#dcdcdc;color:#6d6d6d}
.tabs span.on{background:var(--yellow);color:var(--white)}
.cards{position:absolute;top:220px;left:162px;display:flex;gap:12px}
.card{width:210px;height:350px;background:var(--white);position:relative;text-align:center}
.card-img{height:153px}
.price{position:absolute;top:170px;left:0;width:100%;font-size:21px;font-weight:700;line-height:26px}
.card h3{position:absolute;top:206px;left:0;width:100%;font-size:12.5px;font-weight:600;line-height:18px;color:var(--ink)}
.card p{position:absolute;top:232px;left:16px;right:16px;font-size:10px;line-height:16px;color:var(--muted)}
.btn-more{position:absolute;left:51px;top:298px;width:108px;height:34px;background:var(--ink);color:var(--white);font-size:9.5px;font-weight:700;line-height:34px;border-right:5px solid var(--yellow)}

/* beverage */
.beverage{top:1311px;height:609px;background:linear-gradient(180deg,#3a2a20 0%,#22201e 45%,#1a1816 100%)}
.bev-bg{position:absolute;inset:0;background:radial-gradient(ellipse at 25% 60%,rgba(160,110,50,.25),transparent 55%),radial-gradient(ellipse at 80% 30%,rgba(120,90,60,.2),transparent 55%)}
.bev-cols{position:absolute;top:220px;left:162px;display:flex;gap:17px}
.bev{width:281px;height:324px;background:var(--panel);position:relative;text-align:center;color:var(--white)}
.bev-img{position:absolute;left:70px;top:-71px;width:140px;height:140px;border-radius:50%;border:4px solid var(--white);background:radial-gradient(circle at 50% 55%,#e8a43a,#8a4b12 70%,#3a1f08)}
.bev h4{position:absolute;top:100px;width:100%;font-size:12.5px;font-weight:600;letter-spacing:.3px}
.bev ul{position:absolute;top:134px;left:32px;right:28px;list-style:none}
.bev li{display:flex;align-items:center;height:28px;font-size:10.5px}
.bev li .fill{flex:1;border-bottom:1px solid #555;margin:0 14px 0 10px}
.bev li b{font-size:14px;font-weight:600;width:18px;text-align:right}
.bev.gold b{color:var(--yellow)}

/* bookings */
.bookings{top:1920px;height:535px;background:var(--white)}
.form{position:absolute;top:167px;left:162px;width:876px}
.field{position:absolute;height:43px;background:var(--field);border:1px solid var(--line);font-size:10px;font-style:italic;color:#8a8a8a;padding:13px 0 0 26px}
.field svg{position:absolute;left:10px;top:15px}
.btn-book{position:absolute;left:694px;top:280px;width:182px;height:46px;background:var(--ink);color:var(--white);font-size:14px;font-weight:600;line-height:46px;text-align:center}

/* map */
.map{top:2455px;height:361px;background:linear-gradient(135deg,#e3e3e3,#cfcfcf 60%,#dadada)}
.map-pin{position:absolute;left:596px;top:2596px}

/* footer */
.site-footer{top:2816px;height:331px;background:var(--black);color:#cfcfcf}
.f-title{position:absolute;top:52px;font-family:"Cinzel",Georgia,serif;font-size:17.5px;color:var(--white);letter-spacing:.5px}
.hours{position:absolute;left:162px;top:92px;width:184px;font-size:10px;line-height:19px}
.hours div{display:flex}
.hours .lead{flex:1;border-bottom:1px dotted #888;margin:0 2px 6px}
.contact{position:absolute;left:420px;top:92px;width:190px;font-size:10px;line-height:18px}
.contact li{list-style:none;position:relative;padding-left:20px;margin-bottom:8px}
.contact svg{position:absolute;left:0;top:3px}
.cf{position:absolute;left:646px;top:86px;width:191px}
.cf div{height:26px;margin-bottom:6px;background:#2b2b2b;border:1px solid #3a3a3a;font-size:9px;font-style:italic;color:#888;padding:6px 8px}
.cf .send{background:var(--yellow);color:var(--white);font-style:normal;font-weight:700;text-align:center;border:none;margin-top:8px}
.f-brand{position:absolute;left:906px;top:68px;color:var(--white);font-family:"Cinzel",Georgia,serif;font-weight:600;font-size:24px;line-height:25px}
.social{position:absolute;left:919px;top:186px;display:flex;gap:6px}
.social span{width:25px;height:25px;border:1.5px solid #cfcfcf;border-radius:50%}
.f-rule{position:absolute;left:162px;top:260px;width:876px;border-top:1px solid #2e2e2e}
.copy{position:absolute;top:290px;width:100%;text-align:center;font-size:10px;color:#bdbdbd}
</style>
</head>
<body>

<header class="site-header">
  <div class="brand-small">THE<br>QUIET<br>HOUND</div>
  <nav class="nav">
    <a class="active" href="#">HOME</a>
    <a href="#">FOOD MENU</a>
    <a href="#">BEVERAGE MENU</a>
    <a href="#">BOOKINGS</a>
  </nav>
  <div class="search">
    <svg width="40" height="40" viewBox="0 0 40 40"><circle cx="18.5" cy="18.5" r="5" fill="none" stroke="#111" stroke-width="2"/><line x1="22" y1="22" x2="26" y2="26" stroke="#111" stroke-width="2.4"/></svg>
  </div>
</header>

<section class="hero">
  <div class="hero-photo" role="img" aria-label="Photo of friends raising drinks together at the bar, warm daylight"></div>
  <div class="hero-shade"></div>
  <div class="hero-logo"><span class="the">THE</span><span class="name">QUIET HOUND</span></div>
  <svg class="hero-rule" viewBox="0 0 296 14"><line x1="0" y1="7" x2="296" y2="7" stroke="#fff" stroke-width="1"/><rect x="143" y="2" width="10" height="10" transform="rotate(45 148 7)" fill="#fff"/></svg>
  <p class="hero-text">Lorem ipsum dolor sit amet, consectetur adipiscing elit.<br>Aenean semper orci semper tempus.</p>
  <div class="btn-start">GET STARTED HERE &#10148;</div>
  <div class="dots"><i></i><i></i><i></i><i></i></div>
</section>

<section class="food">
  <div class="deco-plate" role="img" aria-label="Plate of fresh salad" style="right:0;top:-10px;width:120px;height:120px;background:radial-gradient(circle,#9cc06a 0 35%,#f1efe8 36% 100%)"></div>
  <h2 class="sec-title" style="top:42px">FOOD MENU</h2>
  <p class="sec-intro" style="top:96px">Lorem ipsum dolor sit amet, consectetur adipiscing elit. Phasellus lobortis dictum elit eu placeratullam vel pellentesque tortor, nec ornare enim. Praesent vehicula dapibus diam non porttitor. Etiam vel elit ante. Phasellus eleifend sollicitudin odi.</p>
  <div class="tabs"><span class="on">ALL</span><span>SALADS</span><span>MAIN</span><span>DESSERTS</span></div>
  <div class="cards">
    <article class="card"><div class="card-img" role="img" aria-label="Photo of fried shrimp with lemon" style="background:linear-gradient(135deg,#f2c25a,#d07a22)"></div><div class="price">$ 7.80</div><h3>Food lorem ispmdolor site</h3><p>Lorem ipsum dolor sit amet csecte tur adipiscing elit. Phasellus lobortis dictum elit eu placeratullam ve.</p><div class="btn-more">READ MORE &#187;</div></article>
    <article class="card"><div class="card-img" role="img" aria-label="Photo of chicken wings with dipping sauce" style="background:linear-gradient(135deg,#8a4a22,#4a2a16)"></div><div class="price">$ 7.80</div><h3>Food lorem ispmdolor site</h3><p>Lorem ipsum dolor sit amet csecte tur adipiscing elit. Phasellus lobortis dictum elit eu placeratullam ve.</p><div class="btn-more">READ MORE &#187;</div></article>
    <article class="card"><div class="card-img" role="img" aria-label="Photo of fried calamari with dip" style="background:linear-gradient(135deg,#e7d2a8,#b88a4a)"></div><div class="price">$ 7.80</div><h3>Food lorem ispmdolor site</h3><p>Lorem ipsum dolor sit amet csecte tur adipiscing elit. Phasellus lobortis dictum elit eu placeratullam ve.</p><div class="btn-more">READ MORE &#187;</div></article>
    <article class="card"><div class="card-img" role="img" aria-label="Photo of a stacked burger" style="background:linear-gradient(135deg,#d9822e,#7a2e10)"></div><div class="price">$ 7.80</div><h3>Food lorem ispmdolor site</h3><p>Lorem ipsum dolor sit amet csecte tur adipiscing elit. Phasellus lobortis dictum elit eu placeratullam ve.</p><div class="btn-more">READ MORE &#187;</div></article>
  </div>
</section>

<section class="beverage dark">
  <div class="bev-bg" role="img" aria-label="Dim photo of a bar counter with bottles"></div>
  <h2 class="sec-title" style="top:30px">BEVERAGE MENU</h2>
  <p class="sec-intro" style="top:87px">Lorem ipsum dolor sit amet, consectetur adipiscing elit. Phasellus lobortis dictum elit eu placeratullam vel pellentesque tortor, nec ornare enim. Praesent vehicula dapibus diam non porttitor. Etiam vel elit ante. Phasellus eleifend sollicitudin odi.</p>
  <div class="bev-cols">
    <div class="bev gold"><div class="bev-img" role="img" aria-label="Photo of a beer mug"></div><h4>BEVERAGE NAME</h4>
      <ul><li>Datls unde omn<span class="fill"></span><b>27</b></li><li>Raatis unde omn<span class="fill"></span><b>27</b></li><li>Qatis unde omn lore<span class="fill"></span><b>85</b></li><li>Watis uatis unde omnr<span class="fill"></span><b>78</b></li><li>Satis unde omnr<span class="fill"></span><b>78</b></li><li>Watis uatis unde omnr<span class="fill"></span><b>78</b></li></ul></div>
    <div class="bev"><div class="bev-img" role="img" aria-label="Photo of a glass of lager"></div><h4>BEVERAGE NAME</h4>
      <ul><li>Datls unde omn<span class="fill"></span><b>27</b></li><li>Raatis unde omn<span class="fill"></span><b>27</b></li><li>Qatis unde omn lore<span class="fill"></span><b>85</b></li><li>Watis uatis unde omnr<span class="fill"></span><b>78</b></li><li>Satis unde omnr<span class="fill"></span><b>78</b></li><li>Watis uatis unde omnr<span class="fill"></span><b>78</b></li></ul></div>
    <div class="bev"><div class="bev-img" role="img" aria-label="Photo of a whisky glass"></div><h4>BEVERAGE NAME</h4>
      <ul><li>Datls unde omn<span class="fill"></span><b>27</b></li><li>Raatis unde omn<span class="fill"></span><b>27</b></li><li>Qatis unde omn lore<span class="fill"></span><b>85</b></li><li>Watis uatis unde omnr<span class="fill"></span><b>78</b></li><li>Satis unde omnr<span class="fill"></span><b>78</b></li><li>Watis uatis unde omnr<span class="fill"></span><b>78</b></li></ul></div>
  </div>
</section>

<section class="bookings">
  <div class="deco-plate" role="img" aria-label="Plate of salad" style="right:-30px;top:8px;width:130px;height:110px;background:radial-gradient(circle,#8fb85a 0 40%,#f1efe8 41% 100%)"></div>
  <div class="deco-plate" role="img" aria-label="Plate of grilled salmon with salad" style="left:-20px;top:380px;width:170px;height:110px;background:radial-gradient(ellipse,#e07a3a 0 35%,#7aa64a 36% 55%,#f3f1ea 56% 100%)"></div>
  <div class="deco-plate" role="img" aria-label="Cheese board with wine glasses" style="right:-10px;top:370px;width:150px;height:120px;border-radius:40%;background:linear-gradient(135deg,#7a1020 0 25%,#f0d88a 26% 70%,#eae6dc 71%)"></div>
  <h2 class="sec-title" style="top:32px">BOOKINGS ONLINE</h2>
  <p class="sec-intro" style="top:94px">Lorem ipsum dolor sit amet, consectetur adipiscing elit. Phasellus lobortis dictum elit eu placeratullam vel pellentesque tortor, nec ornare enim. Praesent vehicula dapibus diam non porttitor. Etiam vel elit ante. Phasellus eleifend sollicitudin odi.</p>
  <div class="form">
    <div class="field" style="left:0;top:0;width:432px"><svg width="10" height="10" viewBox="0 0 10 10"><circle cx="5" cy="3" r="2.5" fill="#999"/><path d="M0 10c0-3 2-4.5 5-4.5s5 1.5 5 4.5z" fill="#999"/></svg>Name:</div>
    <div class="field" style="left:444px;top:0;width:432px"><svg width="10" height="10" viewBox="0 0 10 10"><rect x="0.5" y="1.5" width="9" height="8" fill="none" stroke="#999"/><line x1="0.5" y1="4" x2="9.5" y2="4" stroke="#999"/></svg>Date:</div>
    <div class="field" style="left:0;top:47px;width:432px"><svg width="10" height="10" viewBox="0 0 10 10"><rect x="0.5" y="1.5" width="9" height="7" fill="none" stroke="#999"/><path d="M0.5 1.5l4.5 4 4.5-4" fill="none" stroke="#999"/></svg>Email:</div>
    <div class="field" style="left:444px;top:47px;width:432px"><svg width="10" height="10" viewBox="0 0 10 10"><circle cx="5" cy="5" r="4.3" fill="none" stroke="#999"/><path d="M5 2.5v2.7l2 1" fill="none" stroke="#999"/></svg>Time:</div>
    <div class="field" style="left:0;top:93px;width:432px"><svg width="10" height="10" viewBox="0 0 10 10"><path d="M2 0.5l2 2-1 1.5c.8 1.6 1.8 2.6 3 3l1.5-1 2 2-1.5 1.5C4 9 1 6 .5 2z" fill="#999"/></svg>Phone:</div>
    <div class="field" style="left:444px;top:93px;width:432px"><svg width="12" height="10" viewBox="0 0 12 10"><circle cx="4" cy="3" r="2" fill="#999"/><circle cx="8.5" cy="3" r="2" fill="#999"/><path d="M0 10c0-3 1.5-4 4-4s4 1 4 4zM6 10c0-3 1.5-4 3-4s3 1 3 4z" fill="#999"/></svg>No of People:</div>
    <div class="field" style="left:0;top:141px;width:876px;height:120px"><svg width="10" height="10" viewBox="0 0 10 10"><path d="M1 9l1-3 5-5 2 2-5 5z" fill="#999"/></svg>Subject:</div>
    <div class="btn-book">BOOKINGS HERE &#187;</div>
  </div>
</section>

<section class="map" role="img" aria-label="Grey street map showing the bar's location"></section>
<svg class="map-pin" width="34" height="48" viewBox="0 0 34 48"><path d="M17 0C7.6 0 0 7.6 0 17c0 12 17 31 17 31s17-19 17-31C34 7.6 26.4 0 17 0z" fill="#111"/><circle cx="17" cy="17" r="6" fill="#fff"/></svg>

<footer class="site-footer">
  <h5 class="f-title" style="left:162px">OPENING HOURS</h5>
  <div class="hours">
    <div>Mon - Fri<span class="lead"></span>10 Am - 8 Pm</div>
    <div>Saturday<span class="lead"></span>10 Am - 9 Pm</div>
    <div>Wednesday<span class="lead"></span>10 Am - 3Pm</div>
    <div>Bar Opening Hours</div>
    <div>Mon - Fri<span class="lead"></span>10 Pm - 4 Am</div>
    <div>Saturday<span class="lead"></span>10 Pm - 3 Pm</div>
    <div>Wednesday<span class="lead"></span>10 Am - 3Pm</div>
  </div>

  <h5 class="f-title" style="left:420px">CONTACT US</h5>
  <ul class="contact">
    <li><svg width="9" height="12" viewBox="0 0 9 12"><path d="M4.5 0A4.5 4.5 0 000 4.5C0 8 4.5 12 4.5 12S9 8 9 4.5A4.5 4.5 0 004.5 0z" fill="#ccc"/><circle cx="4.5" cy="4.5" r="1.6" fill="#111"/></svg>Postal address: PO Box 214, King Street, Newtown NSW 2042</li>
    <li><svg width="10" height="10" viewBox="0 0 10 10"><path d="M2 0.5l2 2-1 1.5c.8 1.6 1.8 2.6 3 3l1.5-1 2 2-1.5 1.5C4 9 1 6 .5 2z" fill="#ccc"/></svg>Phone: 02-5550-1842</li>
    <li><svg width="11" height="10" viewBox="0 0 11 10"><rect x="0" y="3" width="11" height="7" fill="#ccc"/><rect x="2.5" y="0" width="6" height="4" fill="#ccc"/></svg>Fax: 02-5550-1843</li>
    <li><svg width="11" height="9" viewBox="0 0 11 9"><rect x="0.5" y="0.5" width="10" height="8" fill="none" stroke="#ccc"/><path d="M0.5 0.5l5 4 5-4" fill="none" stroke="#ccc"/></svg>hello@quiethound.example</li>
  </ul>

  <h5 class="f-title" style="left:646px">CONTACT FORM</h5>
  <div class="cf">
    <div>Name:</div>
    <div>Phone:</div>
    <div>Message:</div>
    <div class="send">CONTACT &#187;</div>
  </div>

  <div class="f-brand">THE<br>QUIET<br>HOUND</div>
  <div class="social"><span aria-label="Social link one"></span><span aria-label="Social link two"></span><span aria-label="Social link three"></span><span aria-label="Social link four"></span></div>

  <div class="f-rule"></div>
  <p class="copy">&copy; 2016 The Quiet Hound. All copyrights are reserved &nbsp;Term of Use</p>
</footer>

</body>
</html>
```